Tri-Fold Brochure for Substance Abuse Recovery Center

We are looking to freshen up our tri-fold brochure for our recovery facility. Something that helps convey our message of treatment in the great outdoors. I've included a word document with a mock up.

```html
<!DOCTYPE html>
<html lang="en">
<head>
<meta charset="utf-8">
<title>Cedar Ridge Recovery Center – Tri-Fold Brochure</title>
<link href="https://fonts.googleapis.com/css2?family=Montserrat:wght@400;500;600;700;800&display=swap" rel="stylesheet">
<style>
:root{
  --orange:#f39a2e;
  --blue:#3b6d8c;
  --blue-dark:#2c556f;
  --ink:#3d3d3d;
  --paper:#ffffff;
  --bg:#d9d9d9;
}
*{box-sizing:border-box;margin:0;padding:0}
html,body{width:1200px;height:1200px;overflow:hidden;background:var(--bg);font-family:'Montserrat',sans-serif;color:var(--ink)}
.spread{position:absolute;left:60px;width:1080px;height:540px;background:var(--paper);display:flex;box-shadow:0 6px 18px rgba(0,0,0,.18);overflow:hidden}
.spread--outside{top:40px}
.spread--inside{top:620px}
.panel{position:relative;width:360px;height:540px;overflow:hidden}
.panel + .panel{border-left:1px solid #ececec}
.photo{position:absolute}
.section-title{font-weight:700;color:var(--blue);font-size:14px;position:relative;padding-left:14px;margin-bottom:2px}
.section-title::before{content:"";position:absolute;left:0;top:4px;border-left:7px solid var(--orange);border-top:4px solid transparent;border-bottom:4px solid transparent}
.section-title::after{content:"";display:block;width:38px;height:2px;background:var(--orange);margin-top:3px}
.body-text{font-size:9.5px;line-height:1.45;margin-bottom:6px}
.block{margin-bottom:14px}

/* back flap */
.flap-text{position:absolute;left:30px;top:30px;width:300px;z-index:2}
.flap-text .body-text{font-style:italic}
.flap-text .block{margin-bottom:12px}
.flap-photo{left:0;bottom:0;width:360px;height:230px;background:linear-gradient(180deg,#f4f7f9 0%,#9cc2d6 30%,#5a8aa3 58%,#8a6a48 85%,#6b4d33 100%)}
.flap-fade{position:absolute;left:0;top:310px;width:360px;height:60px;background:linear-gradient(#fff,rgba(255,255,255,0))}

/* mailer panel */
.stamp{position:absolute;right:110px;top:26px;width:54px;height:62px;border:1px solid #aaa}
.address-line{position:absolute;left:120px;width:110px;height:1px;background:#aaa}
.contact{position:absolute;left:30px;bottom:40px;width:260px;height:150px;transform-origin:left bottom}
.contact-inner{position:absolute;left:0;top:0;transform:rotate(-90deg) translate(-150px,0);transform-origin:left top;width:240px}
.brand-small{display:flex;align-items:center;gap:6px;font-weight:700;color:var(--orange);font-size:15px;margin-bottom:6px}
.brand-small .dot{width:12px;height:12px;border-radius:50%;background:var(--orange)}
.contact-line{font-size:10px;font-weight:600;display:flex;align-items:center;gap:5px;margin-bottom:3px}
.strip{position:absolute;right:0;top:0;width:120px;height:540px;background:var(--orange)}
.strip-photo{position:absolute;left:10px;width:100px}

/* cover */
.cover-top{position:absolute;left:0;top:0}
.brand{position:absolute;right:26px;top:86px;text-align:right}
.brand-name{display:flex;align-items:center;gap:8px;justify-content:flex-end;font-weight:800;color:var(--blue);font-size:17px}
.brand-name .dot{width:20px;height:20px;border-radius:50%;background:var(--orange)}
.brand-sub{font-size:8px;font-weight:700;letter-spacing:2px;color:var(--blue);margin-top:2px}
.headline{position:absolute;left:20px;right:20px;top:160px;text-align:right}
.headline .h1{font-weight:700;color:var(--orange);font-size:28px;letter-spacing:1px}
.headline .h2{font-weight:500;color:var(--ink);font-size:24px;letter-spacing:1px}
.headline .band{display:inline-block;background:var(--blue);color:#fff;font-weight:700;font-size:14px;padding:4px 10px;letter-spacing:1px;margin-top:4px}
.headline .h3{font-weight:400;color:var(--orange);font-size:26px;letter-spacing:2px;margin-top:2px}
.cover-photo{left:0;bottom:0;width:360px;height:240px;background:linear-gradient(160deg,#6f8fa8 0%,#3d6077 45%,#6f8a3e 75%,#4e6a2c 100%);clip-path:polygon(0 30%,100% 0,100% 100%,0 100%)}
.cover-bar{position:absolute;left:0;bottom:0;width:360px;height:34px;background:var(--blue);color:#fff;font-size:11px;letter-spacing:2px;display:flex;align-items:center;justify-content:center;font-weight:500}

/* inside */
.quote-area{left:0;top:0;width:360px;height:230px;background:linear-gradient(180deg,#3b6d8c 0%,#2c556f 60%,#3f6a58 100%)}
.quote{position:absolute;left:34px;top:48px;width:250px;color:#fff;font-weight:700;font-size:11.5px;line-height:1.35}
.quote-mark{color:var(--orange);font-size:26px;font-weight:800;line-height:.6;display:block}
.quote-by{display:flex;align-items:center;gap:10px;margin-top:6px;color:var(--orange);font-size:11px}
.quote-by::before{content:"";width:60px;height:1px;background:#fff}
.inside-left{position:absolute;left:30px;top:250px;width:300px}
.inside-mid{position:absolute;left:30px;top:130px;width:300px}
.inside-right{position:absolute;left:24px;top:40px;width:320px}
.list{list-style:none;font-size:9.5px;line-height:1.5}
.list li::before{content:"• "}
.columns{display:flex;gap:18px}
.right-photo{right:0;bottom:0;width:360px;height:200px;background:linear-gradient(160deg,#e9d9b8 0%,#9bb0c8 40%,#3b5a8a 70%,#3c6b3d 100%);clip-path:polygon(0 45%,100% 0,100% 100%,0 100%)}
</style>
</head>
<body>

<section class="spread spread--outside">
  <div class="panel panel--flap">
    <div class="photo flap-photo" role="img" aria-label="Couple in plaid shirts embracing on a rocky shore overlooking a lake"></div>
    <div class="flap-fade"></div>
    <div class="flap-text">
      <div class="block">
        <div class="section-title">The Campus:</div>
        <p class="body-text">Cedar Ridge is nestled in the Ohio Valley with 50 acres of scenic tranquility, lakes and forests!</p>
      </div>
      <div class="block">
        <div class="section-title">The Housing:</div>
        <p class="body-text">Our clients reside in spacious mountain view villas, with many comforts. They even have memory foam mattresses!</p>
      </div>
      <div class="block">
        <div class="section-title">Acceptance Process:</div>
        <p class="body-text">Just call! Our admissions team works hard to ensure we can help you improve your life. Please have any insurance information ready when you call for faster admission.</p>
        <p class="body-text">We will even help with transportation.</p>
      </div>
    </div>
  </div>

  <div class="panel panel--mailer">
    <div class="stamp"></div>
    <div class="address-line" style="top:120px"></div>
    <div class="address-line" style="top:145px"></div>
    <div class="address-line" style="top:170px"></div>
    <div class="contact">
      <div class="contact-inner">
        <div class="brand-small"><span class="dot"></span>Cedar Ridge</div>
        <div class="contact-line">
          <svg width="9" height="9" viewBox="0 0 10 10"><path d="M2 1l2 2-1 1.5a6 6 0 0 0 2.5 2.5L7 6l2 2-1.5 1.5C4 9 1 6 .5 2.5z" fill="#f39a2e"/></svg>800-555-0147</div>
        <div class="contact-line">
          <svg width="9" height="9" viewBox="0 0 10 10"><circle cx="5" cy="5" r="4" fill="none" stroke="#f39a2e" stroke-width="1.4"/></svg>www.cedarridgerecovery.com</div>
        <div class="contact-line">
          <svg width="9" height="10" viewBox="0 0 10 12"><path d="M5 11S1 6.5 1 4a4 4 0 0 1 8 0c0 2.5-4 7-4 7z" fill="#f39a2e"/></svg>120 Maple Hollow Rd</div>
        <div class="contact-line" style="padding-left:14px">Fairview, Ohio 45000</div>
      </div>
    </div>
    <div class="strip">
      <div class="photo strip-photo" style="top:12px;height:70px;background:linear-gradient(#7d6a58,#4a3e35)" role="img" aria-label="Villa interior"></div>
      <div class="photo strip-photo" style="top:92px;height:130px;background:linear-gradient(#dfe9ef,#6d8f5a 60%,#4a6a3a)" role="img" aria-label="Forest river landscape"></div>
      <div class="photo strip-photo" style="top:232px;height:110px;background:linear-gradient(#caa16a,#7b5a3e)" role="img" aria-label="Living room interior"></div>
      <div class="photo strip-photo" style="top:352px;height:80px;background:linear-gradient(#5b4b42,#2f2a27)" role="img" aria-label="Bedroom interior"></div>
      <div class="photo strip-photo" style="top:442px;height:80px;background:linear-gradient(#a88a6a,#6d5540)" role="img" aria-label="Dining area"></div>
    </div>
  </div>

  <div class="panel panel--cover">
    <svg class="cover-top" width="360" height="150" viewBox="0 0 360 150">
      <polygon points="0,0 360,0 360,50 180,70 40,90" fill="#3b6d8c"/>
      <polygon points="40,90 20,40 130,70" fill="#f39a2e"/>
    </svg>
    <div class="brand">
      <div class="brand-name">Cedar Ridge<span class="dot"></span></div>
      <div class="brand-sub">RECOVERY CENTER</div>
    </div>
    <div class="headline">
      <div class="h1">A DESTINATION</div>
      <div class="h2">For Recovery</div>
      <div class="band">INSPIRING SOBRIETY &amp;</div>
      <div class="h3">ADVENTURE</div>
    </div>
    <svg style="position:absolute;left:0;bottom:164px" width="360" height="80" viewBox="0 0 360 80"><line x1="0" y1="76" x2="360" y2="4" stroke="#f39a2e" stroke-width="5"/></svg>
    <div class="photo cover-photo" role="img" aria-label="Two hikers with backpacks climbing a grassy slope above a lake"></div>
    <div class="cover-bar">www.cedarridgerecovery.com</div>
  </div>
</section>

<section class="spread spread--inside">
  <svg style="position:absolute;left:0;top:0;z-index:2" width="720" height="130" viewBox="0 0 720 130">
    <path d="M280 0 L720 0 L720 110 C640 40 520 20 360 20 Z" fill="#f39a2e"/>
  </svg>
  <div class="panel">
    <div class="photo quote-area" role="img" aria-label="Rocky coastline with blue water and greenery"></div>
    <div class="quote">
      <span class="quote-mark">“</span>
      Cedar Ridge is not your typical center. Patients don't just sit around all day. There are so many activities that keep them engaged and working on themselves
      <div class="quote-by"><span class="quote-mark" style="display:inline">”</span>Laura M</div>
    </div>
    <div class="inside-left">
      <div class="block">
        <div class="section-title">Who We Are</div>
        <p class="body-text">We are a team with a passion for recovery. We are advocates that care about helping find people the right fit for them...even if it isn't with Cedar Ridge.</p>
        <p class="body-text">However, we feel that Cedar Ridge is the destination recovery center. It allows individuals personal treatment plans, and an unmatched environment.</p>
      </div>
      <div class="block">
        <div class="section-title">Our Philosophy</div>
        <p class="body-text">At Cedar Ridge, we focus on individualized treatment plans to address mental health, medical and emotional needs. We incorporate the Relapse Prevention Program and treat trauma and co-occurring disorders.</p>
      </div>
    </div>
  </div>

  <div class="panel">
    <div class="inside-mid">
      <div class="block">
        <div class="section-title">Relapse Prevention Program</div>
        <p class="body-text">We know the statistics. We want them to change.</p>
        <p class="body-text">Our Relapse Prevention Program offers an intensive 2 week stabilization program for clients.</p>
        <p class="body-text">If a patient has been to treatment before, this is the program for them. Our programs have traditional steps to them, with unique individual therapies and recovery options.</p>
      </div>
      <div class="block">
        <div class="section-title">Improvement</div>
        <p class="body-text">We want EVERYONE to walk out of our facility an improved individual. This includes helping improve credit scores, interviewing skills and family foundations.</p>
        <p class="body-text">Clients learn to reshape their lives with healthy coping skills.</p>
        <p class="body-text">Our HOPE Program offers Heart Centered Healing: Emotionally Focused Therapy.</p>
      </div>
    </div>
  </div>

  <div class="panel">
    <div class="inside-right">
      <div class="block">
        <div class="section-title">Our Program</div>
        <ul class="list">
          <li>A 30 Day Residential Inpatient &amp; Outpatient Treatment</li>
          <li>Ongoing Recovery Care</li>
          <li>Dialectical Behavioral Therapy</li>
          <li>Emotionally Focused Therapy</li>
          <li>Solution Focused Therapy</li>
          <li>Adventure Therapy</li>
        </ul>
      </div>
      <div class="block">
        <div class="section-title">Activities</div>
        <p class="body-text">These really set us apart!</p>
        <div class="columns">
          <ul class="list">
            <li>BIO BED</li><li>ACUPUNCTURE</li><li>WEEKLY IN-HOUSE SALON</li><li>KAYAKING</li><li>HIKING</li><li>FIRE PITS</li><li>BIKING</li>
          </ul>
          <ul class="list">
            <li>YOGA</li><li>FITNESS CENTER</li><li>POOL</li><li>NAVIGATION ROPES COURSES</li><li>ZIP-LINING</li><li>ROCK CLIMBING</li><li>GAMES</li><li>FISHING</li>
          </ul>
        </div>
      </div>
    </div>
    <svg style="position:absolute;left:0;bottom:150px" width="360" height="100" viewBox="0 0 360 100"><line x1="0" y1="96" x2="360" y2="4" stroke="#f39a2e" stroke-width="5"/></svg>
    <div class="photo right-photo" role="img" aria-label="Smiling young couple outdoors by a lake with a wooden dock"></div>
  </div>
</section>

</body>
</html>
```